New Business Card Design Project

I would like to purchase a customized version of a design you have previously submitted - https://www.plorvexa.com/design/7314826<br/><br/>I would like to incorporate the attached Images for my fitness company "TrelmoKor Athletics". My initial services is personal training and athletic performance. I would like a card that has one a shiny black side with the silver logo and the side with a white background utilizing the gold logo. On the white side, put "Sports Performance and Functional Strength Training" under the logo.
Industry/Entity Type
Fitness
Contact Information for Business Card
Quillan Morrow
Owner and Trainer
555.271.9384
quillan.morrow@trelmokorathletics.com
Look and feel
Each slider illustrates characteristics of the customer's brand and the style your logo design should communicate.

```html
<!DOCTYPE html>
<html lang="en">
<head>
<meta charset="utf-8">
<title>TrelmoKor Athletics — Business Card</title>
<link href="https://fonts.googleapis.com/css2?family=Montserrat:wght@500;600;700&family=Roboto:wght@400&display=swap" rel="stylesheet">
<style>
  :root {
    --backdrop: #2b2b2d;
    --card-black: #0a0a0a;
    --card-white: #ffffff;
    --silver: #d4d4d6;
    --silver-dark: #8d8d91;
    --gold: #8c6a2c;
    --gold-light: #b8924a;
    --ink: #222222;
  }
  * { margin: 0; padding: 0; box-sizing: border-box; }
  html, body { width: 1200px; height: 926px; overflow: hidden; }
  body {
    background: var(--backdrop);
    display: flex;
    flex-direction: column;
    align-items: center;
    justify-content: center;
    gap: 40px;
    font-family: "Montserrat", sans-serif;
  }
  .card {
    width: 700px;
    height: 400px;
    position: relative;
    box-shadow: 0 10px 30px rgba(0,0,0,0.45);
  }
  .card--front {
    background: linear-gradient(135deg, #1a1a1a 0%, var(--card-black) 55%, #161616 100%);
    display: flex;
    align-items: center;
    justify-content: center;
  }
  .brand-mark {
    width: 230px;
    height: 230px;
    border-radius: 50%;
    display: flex;
    align-items: center;
    justify-content: center;
    text-align: center;
  }
  .card--front .brand-mark { border: 3px solid var(--silver-dark); }
  .brand-name {
    font-family: "Montserrat", sans-serif;
    font-weight: 700;
    font-size: 22px;
    letter-spacing: 3px;
    text-transform: uppercase;
    line-height: 1.35;
  }
  .card--front .brand-name { color: var(--silver); }
  .card--back { background: var(--card-white); }
  .contact {
    position: absolute;
    left: 48px;
    top: 232px;
  }
  .contact__name {
    font-weight: 700;
    font-size: 28px;
    letter-spacing: 0.5px;
    color: var(--gold);
    text-transform: uppercase;
    line-height: 1;
  }
  .contact__role {
    font-weight: 600;
    font-size: 14px;
    letter-spacing: 0.8px;
    color: var(--ink);
    text-transform: uppercase;
    margin-top: 6px;
  }
  .contact__list { list-style: none; margin-top: 14px; }
  .contact__item {
    display: flex;
    align-items: center;
    gap: 12px;
    font-family: "Roboto", sans-serif;
    font-size: 18px;
    color: var(--ink);
    margin-bottom: 8px;
  }
  .contact__icon { width: 20px; height: 16px; flex: none; }
  .identity {
    position: absolute;
    right: 40px;
    top: 40px;
    width: 260px;
    display: flex;
    flex-direction: column;
    align-items: center;
  }
  .card--back .brand-mark { border: 3px solid var(--gold-light); }
  .card--back .brand-name { color: var(--gold); }
  .tagline {
    margin-top: 22px;
    font-weight: 700;
    font-size: 18px;
    line-height: 1.25;
    color: var(--gold);
    text-align: center;
  }
</style>
</head>
<body>
  <section class="card card--front" aria-label="Card front">
    <div class="brand-mark">
      <span class="brand-name">TrelmoKor<br>Athletics</span>
    </div>
  </section>

  <section class="card card--back" aria-label="Card back">
    <div class="contact">
      <p class="contact__name">Quillan Morrow</p>
      <p class="contact__role">Owner and Trainer</p>
      <ul class="contact__list">
        <li class="contact__item">
          <svg class="contact__icon" viewBox="0 0 20 16" aria-hidden="true">
            <path d="M2 5 C2 2 6 1 10 1 C14 1 18 2 18 5 L15 6 L14 4 L6 4 L5 6 Z" fill="#8c6a2c"/>
            <rect x="4" y="7" width="12" height="8" rx="1.5" fill="#8c6a2c"/>
            <circle cx="10" cy="11" r="2" fill="#fff"/>
          </svg>
          555.271.9384
        </li>
        <li class="contact__item">
          <svg class="contact__icon" viewBox="0 0 20 16" aria-hidden="true">
            <rect x="1" y="2" width="18" height="12" rx="1" fill="#8c6a2c"/>
            <path d="M1 2 L10 9 L19 2" fill="none" stroke="#fff" stroke-width="1.4"/>
          </svg>
          quillan.morrow@trelmokorathletics.com
        </li>
      </ul>
    </div>

    <div class="identity">
      <div class="brand-mark">
        <span class="brand-name">TrelmoKor<br>Athletics</span>
      </div>
      <p class="tagline">Sports Performance and<br>Functional Strength Training</p>
    </div>
  </section>
</body>
</html>
```